Single Page Production Company Site

Clean. Simple. Minimalist site with one page.

No portfolio, just some text to communicate a general overview of what the company does.

We work for a very select group of clients, creating strong brand personalities online. The site is specifically minimal and not communicating too much about what we do.. we have a variety of capabilities to work with clients and prefer to be broad with just a simple landing page as the point of contact for our brand.
Updates

Christmas holidays are coming up, maybe people need some time away from work with family and friends... We can keep working on this and I will provide feedback as quickly as possible, but I understand if designers have other commitments during the coming days. Thanks for your hard work!

Industry/Entity Type

Design Agency

Coding

Coded - Design and coding required

Number of Pages Required

1 page

Font styles to use
Sans Serif

Requirements
Must have
• Clean, bold text headlines.
Nice to have
• Unsure about any images used in the design, would like to see options with or without.

```html
<!DOCTYPE html>
<html lang="en">
<head>
<meta charset="utf-8">
<title>Harbor Lane Studio</title>
<link href="https://fonts.googleapis.com/css2?family=Aleo:ital,wght@1,400;1,700&family=Lato:wght@400;700&display=swap" rel="stylesheet">
<style>
  :root {
    --ink: #111111;
    --rule: #555555;
    --ghost: #dedede;
    --blue: #0072bb;
    --blue-deep: #006a98;
    --gold: #ecc800;
    --field: #c4c4c4;
    --footer: #e0e0e0;
    --white: #ffffff;
  }
  * { margin: 0; padding: 0; box-sizing: border-box; }
  html, body { width: 799px; height: 1200px; overflow: hidden; background: var(--white); }
  body { position: relative; font-family: "Lato", sans-serif; color: var(--ink); }
  .abs { position: absolute; }
  .slab { font-family: "Aleo", serif; font-style: italic; font-weight: 700; }

  /* process */
  .process { position: absolute; left: 0; top: 0; width: 799px; height: 450px; }
  .divider { position: absolute; top: 0; width: 1px; height: 450px; background: var(--rule); }
  .step-title { position: absolute; font-family: "Aleo", serif; font-style: italic; font-weight: 700; line-height: 1; white-space: nowrap; }
  .ghost-letter { position: absolute; font-family: "Aleo", serif; font-style: italic; font-weight: 700; color: var(--ghost); font-size: 68px; line-height: 1; }
  .step-sub { position: absolute; font-size: 13.5px; line-height: 1; white-space: nowrap; }
  .step-copy { position: absolute; width: 122px; font-size: 7.6px; line-height: 10px; }

  /* team */
  .team { position: absolute; left: 0; top: 450px; width: 799px; height: 449px; background: var(--blue); color: var(--gold); }
  .team-title { position: absolute; top: 20px; width: 100%; text-align: center; font-size: 13.5px; }
  .team-lead { position: absolute; top: 39px; width: 100%; text-align: center; font-size: 7.6px; line-height: 10px; }
  .team-lead em { font-family: "Aleo", serif; font-weight: 700; }
  .tile { position: absolute; background: var(--blue-deep); }
  .tile-glyph { position: absolute; font-family: "Aleo", serif; font-style: italic; font-weight: 700; color: var(--gold); line-height: 1; }
  .feature { position: absolute; width: 218px; }
  .feature h2 { font-size: 13.5px; line-height: 1; margin-bottom: 6px; }
  .feature p { font-size: 7.6px; line-height: 10px; }

  /* contact */
  .contact-head { position: absolute; left: 165px; top: 932px; font-size: 13.5px; line-height: 1; }
  .contact-copy { position: absolute; left: 165px; top: 953px; width: 220px; font-size: 7.6px; line-height: 10px; }
  .contact-copy p { margin-bottom: 10px; }
  .mail { position: absolute; left: 415px; top: 921px; font-family: "Aleo", serif; font-size: 7.8px; }
  .field-line { position: absolute; left: 415px; width: 215px; height: 1px; background: var(--field); }
  .field-label { position: absolute; left: 418px; font-size: 7.6px; }
  .message { position: absolute; left: 416px; top: 1042px; width: 214px; height: 55px; border: 1px solid var(--field); padding: 5px 7px; font-size: 7.2px; color: #b0b0b0; }
  .send { position: absolute; left: 596px; top: 1107px; width: 33px; height: 11px; background: var(--field); font-size: 7.6px; text-align: center; line-height: 11px; }

  .footer { position: absolute; left: 0; top: 1146px; width: 799px; height: 54px; background: var(--footer); font-size: 7.6px; text-align: center; line-height: 54px; }
  .arrow { position: absolute; width: 18px; height: 6px; }
</style>
</head>
<body>

<section class="process">
  <div class="divider" style="left:150px"></div>
  <div class="divider" style="left:316px"></div>
  <div class="divider" style="left:482px"></div>
  <div class="divider" style="left:648px"></div>

  <div class="ghost-letter" style="left:208px;top:192px">D</div>
  <div class="ghost-letter" style="left:378px;top:192px">A</div>
  <div class="ghost-letter" style="left:556px;top:192px">I</div>

  <h1 class="step-title" style="left:187px;top:154px;font-size:26px">concept.</h1>
  <svg class="arrow" style="left:288px;top:163px" viewBox="0 0 18 6"><path d="M0 3H17M14 1L17 3L14 5" fill="none" stroke="#111" stroke-width="0.6"/></svg>
  <h1 class="step-title" style="left:357px;top:154px;font-size:30px">create.</h1>
  <svg class="arrow" style="left:452px;top:166px" viewBox="0 0 18 6"><path d="M0 3H17M14 1L17 3L14 5" fill="none" stroke="#111" stroke-width="0.6"/></svg>
  <h1 class="step-title" style="left:494px;top:150px;font-size:33px">complete.</h1>

  <h2 class="step-sub slab" style="left:174px;top:219px">design happens here</h2>
  <p class="step-copy" style="left:174px;top:239px">We are leading the way in design innovation for modern websites. Clean, functional, intuitive websites for progressive businesses.</p>
  <h2 class="step-sub slab" style="left:340px;top:219px">art happens here</h2>
  <p class="step-copy" style="left:340px;top:239px">Building brands through design, we believe that contrast is everything. For industry leaders who set the pace and exceed expectations, we help give the company voice and soul.</p>
  <h2 class="step-sub slab" style="left:506px;top:219px">ideas happen here</h2>
  <p class="step-copy" style="left:506px;top:239px">Clients look to us for unique, exceptional solutions to their technology issues. We bring creativity to the table and solve your business' problems with actionable solutions.</p>
</section>

<section class="team">
  <h1 class="team-title slab">the harbor team.</h1>
  <p class="team-lead">Harbor Lane Studio focuses on creating <em>extraordinary online experiences for extraordinary clients.</em><br>We'll work with you to create the perfect online presence for your brand.</p>

  <div class="tile" style="left:148px;top:78px;width:250px;height:123px">
    <span class="tile-glyph" style="left:82px;top:2px;font-size:118px">S</span>
    <svg class="arrow" style="left:168px;top:59px" viewBox="0 0 18 6"><path d="M0 3H17M14 1L17 3L14 5" fill="none" stroke="#111" stroke-width="0.6"/></svg>
  </div>
  <div class="feature" style="left:415px;top:88px">
    <h2 class="slab">Size is Everything.</h2>
    <p>We don't work in a massive corporate office and we don't have a mailroom. Not that there's anything wrong with that, it's just that we like knowing each other's names, and encourage our clients to know ours. Our small staff has an advantage – our group works more efficiently, more cost-effectively and most importantly, flexible to each client's unique needs. We deliver a range of services found at any agency, with the personal service you should expect.</p>
  </div>

  <div class="feature" style="left:165px;top:219px">
    <h2 class="slab">Our Goal.</h2>
    <p>Harbor Lane Studio brings your brand to life, online. We do it all when it comes to online commerce for retail stores, wholesalers and distributors. Taking your company online introduces a world of opportunity, as well as specific challenges associated with online trade. We'll assist you in establishing a successful online presence and bringing your brand to a worldwide audience.</p>
  </div>
  <div class="tile" style="left:399px;top:201px;width:250px;height:124px">
    <svg class="arrow" style="left:40px;top:61px" viewBox="0 0 18 6"><path d="M18 3H1M4 1L1 3L4 5" fill="none" stroke="#111" stroke-width="0.6"/></svg>
    <span class="tile-glyph" style="left:78px;top:-6px;font-size:124px">O</span>
  </div>

  <div class="tile" style="left:149px;top:326px;width:250px;height:123px">
    <span class="tile-glyph" style="left:96px;top:6px;font-size:110px">?</span>
    <svg class="arrow" style="left:167px;top:58px" viewBox="0 0 18 6"><path d="M0 3H17M14 1L17 3L14 5" fill="none" stroke="#111" stroke-width="0.6"/></svg>
  </div>
  <div class="feature" style="left:415px;top:334px">
    <h2 class="slab">Who's Reed?</h2>
    <p>Reed Calloway, owner of Harbor Lane Studio is not your typical principal. He's worked internationally with both Northgate Media and Linden House publications in photo production for titles including Meridian and Gallery Weekly. Originally from coastal Maine and an allaround New Englander, Reed can often be found sailing during the summer and skiing during winter. He believes that inspiration comes from experiencing the world, not from sitting in a cubicle. But no worries, his biggest fear is being offline, and is always within an arms reach of the Internet.</p>
  </div>
</section>

<section class="contact">
  <div class="ghost-letter" style="left:230px;top:912px;font-size:64px">W</div>
  <h2 class="contact-head slab" style="z-index:1">We get you.</h2>
  <div class="contact-copy">
    <p>Having a website isn't enough. You need to show your customers you understand the socially connected online world we live in.</p>
    <p>We help you create designs that capture the personality of your business and project the image you want your customers to see. Maybe you're a small company looking to sell yourself in the big leagues; maybe you're a big company that wants to look approachable; either way, we can make it happen.</p>
    <p>You'll come across looking professional, unique and strikingly hip all at the same time.</p>
  </div>
  <svg class="arrow" style="left:360px;top:1086px" viewBox="0 0 18 6"><path d="M0 3H17M14 1L17 3L14 5" fill="none" stroke="#111" stroke-width="0.6"/></svg>

  <div class="mail">hello@harborlanestudio.com</div>
  <div class="field-line" style="top:954px"></div>
  <div class="field-label" style="top:956px">name</div>
  <div class="field-line" style="top:983px"></div>
  <div class="field-label" style="top:985px">email</div>
  <div class="field-line" style="top:1013px"></div>
  <div class="field-label" style="top:1015px">phone</div>
  <div class="message">message</div>
  <div class="send">send</div>
</section>

<footer class="footer">© 2018 Bright Node LLC. All Rights Reserved.</footer>

</body>
</html>
```